Oil and Gas Exploration and Production company needs a business card design

We need a business card design using our logo and colors in the logo. We want a mainstream design.

```html
<!DOCTYPE html>
<html lang="en">
<head>
<meta charset="utf-8">
<title>Solara Oil &amp; Gas — Business Card</title>
<link href="https://fonts.googleapis.com/css2?family=PT+Serif:wght@400;700&display=swap" rel="stylesheet">
<style>
  :root {
    --backdrop: #e9e7e4;
    --card-dark: #1d181b;
    --card-light: #ffffff;
    --gold: #d9a21b;
    --ink: #1f1c1d;
    --ink-soft: #2e2a2b;
  }
  * { box-sizing: border-box; margin: 0; padding: 0; }
  html, body {
    width: 1200px; height: 900px; overflow: hidden;
    background: var(--backdrop);
    font-family: "PT Serif", Georgia, serif;
  }
  .canvas {
    width: 1200px; height: 900px;
    display: flex; flex-direction: column;
    align-items: center; justify-content: center; gap: 40px;
  }
  .card {
    position: relative;
    width: 700px; height: 400px;
    overflow: hidden;
    box-shadow: 0 6px 18px rgba(0,0,0,0.18);
  }
  /* Front */
  .card-front { background: var(--card-dark); }
  .front-arcs { position: absolute; inset: 0; }
  .front-brand {
    position: absolute; inset: 0;
    display: flex; align-items: center; justify-content: center;
    color: var(--gold);
    font-weight: 700; font-size: 44px; letter-spacing: 0.5px;
  }
  /* Back */
  .card-back { background: var(--card-light); color: var(--ink); }
  .back-brand {
    position: absolute; top: 58px; right: 56px;
    display: flex; align-items: center; gap: 12px;
    font-weight: 700; font-size: 34px; color: var(--ink);
  }
  .brand-dot {
    width: 22px; height: 22px; border-radius: 50%;
    background: var(--gold);
  }
  .holder {
    position: absolute; left: 56px; bottom: 56px;
  }
  .holder-name { font-weight: 700; font-size: 24px; line-height: 1.1; }
  .holder-title {
    font-weight: 700; font-size: 13px; letter-spacing: 1px;
    color: var(--gold); text-transform: uppercase; margin-top: 4px;
  }
  .contact-list { list-style: none; margin-top: 18px; }
  .contact-list li {
    display: flex; align-items: center; gap: 10px;
    font-size: 20px; line-height: 1.35; color: var(--ink-soft);
  }
  .contact-icon { width: 18px; height: 18px; flex: none; }
  .office {
    position: absolute; right: 56px; bottom: 150px;
    text-align: right; font-size: 18px; line-height: 1.35; color: var(--ink-soft);
  }
</style>
</head>
<body>
<main class="canvas">
  <section class="card card-front" aria-label="Card front">
    <svg class="front-arcs" viewBox="0 0 700 400" aria-hidden="true">
      <path d="M 560 10 A 260 260 0 0 1 700 150" fill="none" stroke="var(--gold)" stroke-width="7" stroke-linecap="round"/>
      <path d="M 40 250 A 260 260 0 0 0 170 395" fill="none" stroke="var(--gold)" stroke-width="7" stroke-linecap="round"/>
    </svg>
    <div class="front-brand">Solara Oil &amp; Gas</div>
  </section>

  <section class="card card-back" aria-label="Card back">
    <div class="back-brand"><span class="brand-dot"></span>Solara Oil &amp; Gas</div>

    <address class="office">
      48 Ridgeline Avenue<br>
      Brookfield, Texas 75001<br>
      www.solaraoilgas.com
    </address>

    <div class="holder">
      <p class="holder-name">Daniel Harrow</p>
      <p class="holder-title">Managing Director</p>
      <ul class="contact-list">
        <li>
          <svg class="contact-icon" viewBox="0 0 18 18" aria-label="Phone"><circle cx="9" cy="9" r="9" fill="var(--gold)"/><path d="M5.5 5.5c.6-.6 1.2-.5 1.6 0l.8 1c.3.4.2.9-.1 1.2l-.5.4c.5 1 1.2 1.7 2.2 2.2l.4-.5c.3-.3.8-.4 1.2-.1l1 .8c.5.4.6 1 0 1.6-.8.8-2.2.9-4-.6-1.7-1.5-3.4-3.5-2.6-6z" fill="var(--card-dark)"/></svg>
          555 210 48 76
        </li>
        <li>
          <svg class="contact-icon" viewBox="0 0 18 18" aria-label="Mobile"><circle cx="9" cy="9" r="9" fill="var(--gold)"/><rect x="6.2" y="4" width="5.6" height="10" rx="1" fill="var(--card-dark)"/><rect x="7" y="5.2" width="4" height="6.6" fill="var(--gold)"/></svg>
          555 390 62 14
        </li>
        <li>
          <svg class="contact-icon" viewBox="0 0 18 18" aria-label="Email"><circle cx="9" cy="9" r="9" fill="var(--gold)"/><rect x="4.5" y="6" width="9" height="6.5" fill="var(--card-dark)"/><path d="M4.5 6l4.5 3.6L13.5 6" fill="none" stroke="var(--gold)" stroke-width="1"/></svg>
          d.harrow@solaraoilgas.com
        </li>
      </ul>
    </div>
  </section>
</main>
</body>
</html>
```